Corvane Electronics, Inc. Business card

Incorporate a globe.
We repair electronics, sell electronic parts, and we recycle electronics. We've been in business since 1982. A technology feel to the card is preferred. I want to be able to give this card to a client from different industries and make it relate-able. I don't have a logo that I've been partial to in the past. It is not necessary in this case.

Target Market(s)

Consumer, Industrial, Business, Medical

Industry/Entity Type

Business

Contact Information for Business Card

4518 Maple Crest Blvd. Dallas, TX 75207
214-555-0187 main 214-555-0143 fax
Paul Bredesen VP

Font styles to use
Serif

Requirements
Must have
• Technology feel
Nice to have
• Metallic look
Should not have
• no pastel colors

```html
<!DOCTYPE html>
<html lang="en">
<head>
<meta charset="utf-8">
<title>Corvane Electronics, Inc. — Business Card</title>
<link rel="stylesheet" href="https://fonts.googleapis.com/css2?family=PT+Sans:wght@400&display=swap">
<style>
  :root {
    --stage: #2b2522;
    --ink: #1b1d22;
    --night: #050608;
    --deep-blue: #0a2a7a;
    --glow-blue: #1e6bff;
    --cyan: #4fc3ff;
    --steel-light: #eef0f2;
    --steel-mid: #c3c7cc;
    --steel-dark: #8e949b;
    --rule: #0d0f14;
    --card-w: 540px;
    --card-h: 309px;
  }
  * { box-sizing: border-box; margin: 0; padding: 0; }
  html, body {
    width: 1200px; height: 576px; overflow: hidden;
    background: var(--stage);
    font-family: "PT Sans", "Helvetica Neue", Arial, sans-serif;
  }
  .stage {
    position: relative; width: 1200px; height: 576px;
    display: flex; align-items: center; justify-content: center; gap: 40px;
  }
  .card {
    position: relative; width: var(--card-w); height: var(--card-h);
    overflow: hidden; border-radius: 3px;
    box-shadow: 0 10px 24px rgba(0,0,0,.55);
  }
  .brushed-steel {
    background:
      repeating-linear-gradient(0deg, rgba(255,255,255,.08) 0 1px, rgba(0,0,0,.04) 1px 2px),
      linear-gradient(100deg, var(--steel-dark) 0%, var(--steel-light) 35%, var(--steel-mid) 55%, var(--steel-light) 75%, var(--steel-dark) 100%);
  }
  .divider-rule {
    position: absolute; left: 0; right: 0; height: 6px;
    background: linear-gradient(var(--steel-light) 0 2px, var(--rule) 2px 4px, var(--steel-mid) 4px);
  }

  /* Front */
  .front-circuit-art {
    position: absolute; left: 0; top: 0; width: 100%; height: 66%;
    background:
      radial-gradient(circle at 50% 48%, var(--cyan) 0 5%, var(--glow-blue) 10%, var(--deep-blue) 32%, transparent 58%),
      linear-gradient(90deg, var(--night) 0%, #07132f 45%, var(--night) 100%);
  }
  .front-band {
    position: absolute; left: 0; bottom: 0; width: 100%; height: 34%;
    display: flex; align-items: center; justify-content: center;
  }
  .front-band .divider-rule { top: 0; }
  .company-name {
    font-size: 30px; letter-spacing: 1px; color: var(--ink);
    text-transform: uppercase; padding-top: 6px;
  }

  /* Back */
  .back-top {
    position: absolute; left: 0; top: 0; width: 100%; height: 58%;
  }
  .globe-art {
    position: absolute; left: 52%; top: 8%; width: 190px; height: 190px;
    border-radius: 50%;
    background: radial-gradient(circle at 40% 40%, rgba(255,255,255,.85), rgba(200,204,210,.55) 60%, rgba(150,156,164,.35));
  }
  .back-band {
    position: absolute; left: 0; bottom: 0; width: 100%; height: 42%;
    background:
      radial-gradient(ellipse at 35% 30%, rgba(30,107,255,.55), transparent 55%),
      var(--night);
  }
  .back-band .divider-rule { top: 0; }
  .contact-block {
    position: absolute; left: 50%; top: 30px; color: var(--ink);
  }
  .contact-name { font-size: 20px; margin-bottom: 12px; }
  .contact-line { font-size: 14px; line-height: 1.2; }
</style>
</head>
<body>
<main class="stage">
  <section class="card card-front brushed-steel">
    <div class="front-circuit-art" role="img" aria-label="Glowing blue globe over circuit lines on a dark background"></div>
    <div class="front-band brushed-steel">
      <span class="divider-rule"></span>
      <h1 class="company-name">Corvane Electronics, Inc.</h1>
    </div>
  </section>

  <section class="card card-back">
    <div class="back-top brushed-steel">
      <div class="globe-art" role="img" aria-label="Faint silver wireframe globe"></div>
    </div>
    <div class="back-band" role="img" aria-label="Blue circuit lines glowing on a black band">
      <span class="divider-rule"></span>
    </div>
    <address class="contact-block" style="font-style:normal">
      <p class="contact-name">Paul Bredesen VP</p>
      <p class="contact-line">4518 Maple Crest Blvd.</p>
      <p class="contact-line">Dallas, TX 75207</p>
      <p class="contact-line">Phone: 214-555-0187</p>
      <p class="contact-line">Fax: 214-555-0143</p>
    </address>
  </section>
</main>
</body>
</html>
```